Tello Haulage Junk Removal Postcard

I am looking to have a postcard made for my junk removal company. Details:
size: 6"x9"
I would like to keep it clean and simple. Our company colors are pink, blue and white. You can find the colors and info on the company and what we do on our website which is www.tellohaulage.example .
I've attached a sample of a postcard that was made on ArtHive for another junk removal company. I like the way the attached one looks.

```html
<!DOCTYPE html>
<html lang="en">
<head>
<meta charset="utf-8">
<title>Tello Haulage Junk Removal Postcard</title>
<link rel="stylesheet" href="https://fonts.googleapis.com/css2?family=Poppins:wght@300;700;800&family=Montserrat:wght@800&display=swap">
<style>
  :root {
    --stage: #d4d4d6;
    --card-dark: #1f1f21;
    --card-mid: #3a3a3d;
    --pink: #e5197f;
    --blue: #1d5aa3;
    --white: #ffffff;
  }
  * { margin: 0; padding: 0; box-sizing: border-box; }
  html, body {
    width: 1200px;
    height: 960px;
    overflow: hidden;
    background: var(--stage);
  }
  .postcard {
    position: absolute;
    left: 300px;
    top: 30px;
    width: 600px;
    height: 900px;
    overflow: hidden;
    background: var(--card-dark);
    font-family: "Poppins", sans-serif;
    color: var(--white);
  }
  .backdrop-photo {
    position: absolute;
    inset: 0;
    background:
      radial-gradient(ellipse at 35% 40%, #505054 0%, transparent 55%),
      radial-gradient(ellipse at 60% 80%, #444447 0%, transparent 50%),
      linear-gradient(160deg, var(--card-mid) 0%, var(--card-dark) 100%);
  }
  .brand {
    position: absolute;
    left: 40px;
    top: 44px;
    display: flex;
    align-items: center;
    gap: 10px;
  }
  .brand-square {
    width: 22px;
    height: 22px;
    background: var(--white);
  }
  .brand-name {
    font-weight: 700;
    font-size: 22px;
    letter-spacing: 0.2px;
  }
  .tagline {
    position: absolute;
    right: 40px;
    top: 48px;
    text-align: right;
    font-weight: 300;
    font-size: 26px;
    line-height: 1.25;
  }
  .services {
    position: absolute;
    left: 330px;
    right: 0;
    top: 170px;
    list-style: none;
    display: flex;
    flex-direction: column;
    gap: 12px;
  }
  .service {
    height: 50px;
    padding-left: 24px;
    display: flex;
    align-items: center;
    border-radius: 8px 0 0 8px;
    font-family: "Montserrat", sans-serif;
    font-weight: 800;
    font-size: 20px;
    letter-spacing: 2px;
    text-transform: uppercase;
  }
  .service--pink { background: var(--pink); }
  .service--blue { background: var(--blue); }
  .headline {
    position: absolute;
    left: 40px;
    bottom: 60px;
    line-height: 1.05;
  }
  .headline-lead {
    display: block;
    font-weight: 300;
    font-size: 68px;
  }
  .headline-main {
    display: block;
    font-weight: 800;
    font-size: 76px;
    letter-spacing: -1px;
  }
  .headline-accent { color: var(--pink); }
</style>
</head>
<body>
  <article class="postcard">
    <div class="backdrop-photo" role="img" aria-label="Black and white photo of a pile of junk: old tyres, pipes and scrap metal"></div>

    <div class="brand">
      <span class="brand-square"></span>
      <span class="brand-name">Tello Haulage</span>
    </div>

    <p class="tagline">Let Us Take<br>The Trash Out</p>

    <ul class="services">
      <li class="service service--pink">Residential</li>
      <li class="service service--blue">Commercial</li>
      <li class="service service--pink">Outside</li>
      <li class="service service--blue">Curbside</li>
      <li class="service service--pink">Other</li>
    </ul>

    <h1 class="headline">
      <span class="headline-lead">Relax.</span>
      <span class="headline-main">We Do The</span>
      <span class="headline-main"><span class="headline-accent">Dirty</span> Work</span>
    </h1>
  </article>
</body>
</html>
```